Business card/ logo for alternative health care practice.

Natural health care practiceKinesiologyFunctional medicineEmphasis that healing takes place when a new point of view is achieved. Perspective shift. Acupuncture. Homeopathy. Chiropractic
Law of attraction

Target Market(s)

All sirts

Contact Information for Business Card

Viewpoint Wellness5910 Gunbarrel Ave #EBoulder, CO 80417(303) 442-2142

Font styles to use
Sans Serif

Requirements
Nice to have
• A logo or visual that might depict someone in an improved perspective or point of view

```html
<!DOCTYPE html>
<html lang="en">
<head>
<meta charset="utf-8">
<title>Clearbrook Wellness — Business Card</title>
<link rel="stylesheet" href="https://fonts.googleapis.com/css2?family=Open+Sans:wght@300;400&display=swap">
<style>
  :root {
    --backdrop: #1c1c1c;
    --card: #333333;
    --card-edge: #262626;
    --ink: #f4f4f4;
    --ink-soft: #e6e6e6;
    --accent-green: #8cc63f;
    --divider: #424242;
  }
  * { margin: 0; padding: 0; box-sizing: border-box; }
  html, body {
    width: 1200px;
    height: 900px;
    overflow: hidden;
    background: var(--backdrop);
    font-family: "Open Sans", sans-serif;
  }
  .stage {
    width: 1200px;
    height: 900px;
    display: flex;
    align-items: center;
    justify-content: center;
    gap: 40px;
  }
  .card {
    position: relative;
    width: 500px;
    height: 286px;
    background: var(--card);
    border-radius: 22px;
    box-shadow: 0 3px 0 var(--card-edge), 0 10px 24px rgba(0, 0, 0, 0.35);
    overflow: hidden;
  }

  /* Contact side */
  .card-contact .brand {
    position: absolute;
    left: 0;
    top: 0;
    width: 262px;
    height: 286px;
    display: flex;
    flex-direction: column;
    align-items: center;
    justify-content: center;
    gap: 16px;
  }
  .brand-dot {
    width: 104px;
    height: 104px;
    border-radius: 50%;
    border: 6px solid var(--ink);
    background: var(--card);
  }
  .brand-name {
    color: var(--ink);
    font-size: 17px;
    font-weight: 300;
    letter-spacing: 0.4px;
  }
  .card-contact .divider {
    position: absolute;
    left: 262px;
    top: 34px;
    width: 1px;
    height: 218px;
    background: var(--divider);
  }
  .card-contact .details {
    position: absolute;
    left: 294px;
    top: 100px;
    color: var(--ink-soft);
    font-size: 15px;
    font-weight: 400;
    font-style: normal;
    line-height: 1.55;
  }
  .details .phone {
    display: flex;
    align-items: center;
    gap: 8px;
    margin-bottom: 12px;
  }
  .details .phone svg { width: 13px; height: 13px; flex: none; }

  /* Name side */
  .card-name {
    display: flex;
    align-items: center;
    justify-content: center;
  }
  .wordmark {
    display: flex;
    flex-direction: column;
    align-items: flex-end;
    color: var(--ink);
    font-weight: 300;
    transform: translateY(-18px);
  }
  .wordmark-main {
    font-size: 50px;
    line-height: 1;
    letter-spacing: 0.5px;
  }
  .wordmark-sub {
    font-size: 17px;
    line-height: 1;
    letter-spacing: 2.5px;
    margin-top: 6px;
  }
</style>
</head>
<body>
  <main class="stage">
    <section class="card card-contact">
      <div class="brand">
        <div class="brand-dot"></div>
        <span class="brand-name">Clearbrook Wellness</span>
      </div>
      <div class="divider"></div>
      <address class="details">
        <div class="phone">
          <svg viewBox="0 0 24 24" aria-hidden="true">
            <path fill="var(--accent-green)" d="M6.6 10.8a15.1 15.1 0 0 0 6.6 6.6l2.2-2.2a1 1 0 0 1 1-.25 11.4 11.4 0 0 0 3.6.57 1 1 0 0 1 1 1V20a1 1 0 0 1-1 1A17 17 0 0 1 3 4a1 1 0 0 1 1-1h3.5a1 1 0 0 1 1 1c0 1.25.2 2.45.57 3.57a1 1 0 0 1-.25 1z"/>
          </svg>
          <span>(303) 618-5907</span>
        </div>
        <div>2487 Larkspur Ave</div>
        <div>#C Boulder, CO 80417</div>
      </address>
    </section>
    <section class="card card-name">
      <div class="wordmark">
        <span class="wordmark-main">Clearbrook</span>
        <span class="wordmark-sub">WELLNESS</span>
      </div>
    </section>
  </main>
</body>
</html>
```